Harbor Lantern Productions Business Logo and Card Design

PLEASE LIMIT your submission to maximum of 2 at a time.
Harbor Lantern Productions provides video production services, and produces videos, that help people connect in the spirit of unity and peace.Primarily I am looking for a logo that is simple to remember but the concept is fairly complex. The concept of the logo is a peace dove with an olive branch in it's mouth has it's wings around earth, symbolising that it is protecting earth with peace. If possible I'd like this logo done and delivered in high quality vector format, so I can use it for banners etc.Then the business card I just want a simple white card with the logo in the middle and contact info under the logo. Open to suggestions if you think there should be anything else included, but it must remain simple and uncluttered. Also incorporate something in the logo that says film and video e.g.: film strip or camera lens

Contact Information for Business Card

Harbor Lantern Productions
www.harborlantern.example
teodor@harborlantern.example
+61 478 315 064

Requirements
Must have
• Logo must have the following:
• Peace Dove
• Olive branch
• Earth
• Something about video production (e.g.: film strip or camera lens or anything film related)

```html
<!DOCTYPE html>
<html lang="en">
<head>
<meta charset="utf-8">
<title>Harbor Lantern Productions — Business Card</title>
<link rel="stylesheet" href="https://fonts.googleapis.com/css2?family=Oswald:wght@500&display=swap">
<style>
  :root {
    --backdrop: #e6e4e1;
    --card-paper: #f7f7f6;
    --ink: #121212;
    --swoosh: #141414;
    --swoosh-soft: #2a2a2a;
  }
  * { margin: 0; padding: 0; box-sizing: border-box; }
  html, body {
    width: 1200px;
    height: 970px;
    overflow: hidden;
    background: var(--backdrop);
  }
  .business-card {
    position: absolute;
    left: 100px;
    top: 207px;
    width: 1000px;
    height: 556px;
    background: var(--card-paper);
    box-shadow: 0 18px 40px rgba(0, 0, 0, 0.18);
    overflow: hidden;
    font-family: "Oswald", "Arial Narrow", sans-serif;
    font-weight: 500;
    color: var(--ink);
  }
  .card-swooshes {
    position: absolute;
    inset: 0;
    width: 100%;
    height: 100%;
  }
  .swoosh-main { fill: var(--swoosh); }
  .swoosh-accent { fill: var(--swoosh-soft); }
  .brand-block {
    position: absolute;
    left: 0;
    right: 0;
    top: 98px;
    text-align: center;
  }
  .brand-mark {
    display: block;
    width: 58px;
    height: 58px;
    margin: 0 auto 18px;
    border-radius: 50%;
    background: var(--ink);
  }
  .brand-name {
    font-size: 52px;
    line-height: 1;
    letter-spacing: 0.32em;
    margin-right: -0.32em;
    text-transform: uppercase;
  }
  .brand-sub {
    font-size: 28px;
    line-height: 1;
    margin-top: 8px;
    letter-spacing: 0.18em;
    margin-right: -0.18em;
    text-transform: uppercase;
  }
  .contact-line {
    position: absolute;
    left: 0;
    right: 0;
    top: 356px;
    text-align: center;
    font-size: 26px;
    letter-spacing: 0.03em;
    padding-left: 40px;
  }
  .contact-phone {
    position: absolute;
    left: 0;
    right: 0;
    top: 398px;
    display: flex;
    justify-content: center;
    align-items: center;
    gap: 12px;
    font-size: 38px;
    letter-spacing: 0.04em;
    padding-right: 30px;
  }
  .phone-icon { width: 36px; height: 28px; fill: var(--ink); }
</style>
</head>
<body>
  <div class="business-card">
    <svg class="card-swooshes" viewBox="0 0 1000 556" preserveAspectRatio="none" aria-hidden="true">
      <path class="swoosh-main" d="M681,0 L1000,0 L1000,228 C930,118 820,32 681,0 Z"/>
      <path class="swoosh-main" d="M841,109 C925,160 978,240 1000,334 L1000,262 C962,190 912,140 841,109 Z"/>
      <path class="swoosh-main" d="M0,321 C85,425 190,510 297,556 L0,556 Z"/>
      <path class="swoosh-accent" d="M0,258 C40,330 100,382 160,410 C100,368 42,318 0,284 Z"/>
    </svg>

    <div class="brand-block">
      <span class="brand-mark" aria-hidden="true"></span>
      <div class="brand-name">Harbor Lantern</div>
      <div class="brand-sub">Productions</div>
    </div>

    <div class="contact-line">www.harborlantern.example&nbsp;&nbsp;teodor@harborlantern.example</div>

    <div class="contact-phone">
      <svg class="phone-icon" viewBox="0 0 36 28" aria-hidden="true">
        <path d="M2,9 C2,4 8,2 18,2 C28,2 34,4 34,9 L34,11 L26,11 L25,7 L11,7 L10,11 L2,11 Z"/>
        <path d="M9,12 L27,12 L32,26 L4,26 Z"/>
      </svg>
      <span>+61 478 315 064</span>
    </div>
  </div>
</body>
</html>
```